Multi-Faceted Legal and Finanacial Advisory Group Needs Business Card Design

We need a business card design for a newly branded Orlando Florida area advising group consisting of Attorneys, Accountants and Financial Planners. The company is named RT Counsel Group. You will find our initial work on a business card. The information on the business card are merely guideposts and not final product. The logo does not have the be the same as provided since we have not finalized the logo. We would like to stay with a black/white/grey color scheme, but limited use of color is not out of the question.

Target Market(s)

Businesses and their Corporate Representatives

Industry/Entity Type

Business

Contact Information for Business Card

Should have Name, Title, Phone, Cell, Fax, Email and website. Logo should incorporate RT in some fashion however final logo used does not have to be the one on the document provided.

Requirements
Must have
• An RT design on front and back.

```html
<!DOCTYPE html>
<html lang="en">
<head>
<meta charset="utf-8">
<title>RT Counsel Group – Business Card</title>
<link rel="stylesheet" href="https://fonts.googleapis.com/css2?family=EB+Garamond:ital,wght@0,400;0,600;0,700;1,400&display=swap">
<style>
  :root {
    --page: #ffffff;
    --ink: #111111;
    --ink-soft: #333333;
    --grey-dark: #9a9a9a;
    --grey-mid: #c4c4c4;
    --grey-light: #e6e6e6;
  }
  * { box-sizing: border-box; margin: 0; padding: 0; }
  html, body {
    width: 1200px; height: 750px; overflow: hidden;
    background: var(--page);
    font-family: "EB Garamond", Georgia, serif;
    color: var(--ink);
  }
  .canvas { position: relative; width: 1200px; height: 750px; }

  .card { position: absolute; width: 362px; height: 200px; background: var(--page); }
  .card--front { left: 55px; top: 99px; }
  .card--back { left: 52px; top: 388px; }

  .tone-field { position: absolute; }
  .card--front .tone-field {
    right: 0; top: 0; width: 175px; height: 200px;
    background: linear-gradient(to left, var(--grey-dark) 0%, var(--grey-mid) 45%, var(--grey-light) 80%, rgba(255,255,255,0) 100%);
  }
  .card--back .tone-field {
    left: 0; top: 0; width: 160px; height: 200px;
    background: linear-gradient(to right, var(--grey-dark) 0%, var(--grey-mid) 45%, var(--grey-light) 80%, rgba(255,255,255,0) 100%);
  }

  .holder { position: absolute; left: 10px; top: 14px; }
  .holder__name { font-size: 17px; font-weight: 700; line-height: 1.1; }
  .holder__title { font-size: 15px; font-style: italic; line-height: 1.2; padding-left: 1px; }

  .contact { position: absolute; left: 6px; top: 57px; list-style: none; font-size: 11.5px; color: var(--ink-soft); }
  .contact li { display: flex; align-items: flex-start; gap: 4px; line-height: 13px; margin-bottom: 12px; }
  .contact li.contact__address { margin-bottom: 11px; }
  .contact svg { width: 12px; height: 12px; flex: none; margin-top: 1px; }

  .brand-mark {
    position: absolute; right: 28px; top: 62px;
    display: flex; flex-direction: column; align-items: center; gap: 6px;
  }
  .brand-mark__square { width: 26px; height: 26px; border: 2px solid var(--ink); background: var(--page); }
  .brand-mark__name { font-size: 17px; font-weight: 600; color: var(--ink); text-align: center; line-height: 1.05; width: 110px; }

  .identity { position: absolute; left: 14px; top: 62px; display: flex; align-items: center; gap: 14px; }
  .identity__square { width: 60px; height: 60px; border: 2px solid var(--ink); background: var(--page); flex: none; }
  .identity__name { font-size: 25px; font-weight: 400; letter-spacing: 0.5px; line-height: 1; white-space: nowrap; }
  .identity__tagline { font-size: 11px; letter-spacing: 0.9px; margin-top: 6px; color: var(--ink-soft); white-space: nowrap; }
</style>
</head>
<body>
<main class="canvas">

  <section class="card card--front" aria-label="Business card front">
    <div class="tone-field" role="img" aria-label="Grey square tile pattern fading to white"></div>

    <div class="holder">
      <p class="holder__name">Daniel R. xxxxx, Esq.</p>
      <p class="holder__title">Attorney</p>
    </div>

    <ul class="contact">
      <li class="contact__address">
        <svg viewBox="0 0 12 12" aria-hidden="true"><path d="M1 6 L6 1.5 L11 6 M2.5 5 V10.5 H9.5 V5" fill="none" stroke="currentColor" stroke-width="1.2"/><rect x="5" y="7.5" width="2" height="3" fill="currentColor"/></svg>
        <span>2210 Harbor Point Drive, Suite 340<br>Winter Park, FL 32789</span>
      </li>
      <li>
        <svg viewBox="0 0 12 12" aria-hidden="true"><path d="M2.5 1 L4.5 1 L5.3 3.5 L4 4.6 C4.8 6.3 5.7 7.2 7.4 8 L8.5 6.7 L11 7.5 L11 9.5 C11 10.4 10.2 11 9.3 11 C4.7 10.6 1.4 7.3 1 2.7 C1 1.8 1.6 1 2.5 1 Z" fill="currentColor"/></svg>
        <span>Office: (407) xxx-xxxx</span>
      </li>
      <li>
        <svg viewBox="0 0 12 12" aria-hidden="true"><rect x="3.5" y="0.8" width="5" height="10.4" rx="1" fill="none" stroke="currentColor" stroke-width="1.1"/><rect x="4.6" y="2.2" width="2.8" height="4" fill="currentColor"/></svg>
        <span>Cell: (407) xxx-xxxx</span>
      </li>
      <li>
        <svg viewBox="0 0 12 12" aria-hidden="true"><rect x="1" y="2.5" width="10" height="7" fill="none" stroke="currentColor" stroke-width="1.1"/><path d="M1 2.5 L6 6.5 L11 2.5" fill="none" stroke="currentColor" stroke-width="1.1"/></svg>
        <span>Email: xxxxx@rtcounsel.com</span>
      </li>
      <li>
        <svg viewBox="0 0 12 12" aria-hidden="true"><circle cx="6" cy="6" r="5" fill="none" stroke="currentColor" stroke-width="1.1"/><ellipse cx="6" cy="6" rx="2.2" ry="5" fill="none" stroke="currentColor" stroke-width="0.9"/><path d="M1 6 H11 M2 3.5 H10 M2 8.5 H10" stroke="currentColor" stroke-width="0.8"/></svg>
        <span>Web: www.rt-counsel.com</span>
      </li>
    </ul>

    <div class="brand-mark">
      <span class="brand-mark__square" aria-hidden="true"></span>
      <span class="brand-mark__name">RT Counsel Group</span>
    </div>
  </section>

  <section class="card card--back" aria-label="Business card back">
    <div class="tone-field" role="img" aria-label="Grey square tile pattern fading to white"></div>

    <div class="identity">
      <span class="identity__square" aria-hidden="true"></span>
      <div>
        <p class="identity__name">RT COUNSEL GROUP</p>
        <p class="identity__tagline">Attorneys - Accountants - Financial Planners</p>
      </div>
    </div>
  </section>

</main>
</body>
</html>
```